Sidewalk Sign For Laundry Service

I'd like to make a sign that offers *free* laundry service for the next customers that bring in their laundry. There needs to be some immediacy in the design. The idea is to put out this sign when we are idle in the laundry and want to use the time to attract new customers. So somehow we need to communicate that the offer is for right now and will likely be gone in an hour or two. Attached are photos of the sign holder in place to give a feel for the location and environment. Obviously I'm looking for a much better design that the one currently in use.

Requirements:
* 23.25" x 35.5" - the full width will be visible but the top and bottom 0.5" will be hidden by the sign holder. It will be printed on coroplast.
* Must include a large arrow to show where the service is offered. We're off the main street so the arrow helps a lot. See the attached pictures of the sign being replaced.
* Needs to be visible to cars as they drive by.
* For the final product I'll need three versions. One with an arrow pointing to the right, one with an arrow pointing to the left, and one to go in the store window with no arrow.

Background on the service: We sort, wash, dry, and fold the laundry for customers and then neatly put it in a nice laundry bag that makes returning very convenient. Their laundry comes out fresh, clean, smelling great, and without the hassle of doing it themselves. We have a great return rate. Most customers that try out the service become long term customers.

Attached are two pictures of the sign holder with our current "Laundry Wash & Fold" sign. Also, our logo which would be nice to include to help with branding.

```html
<!DOCTYPE html>
<html lang="en">
<head>
<meta charset="utf-8">
<title>Fresh Fold Laundry – Free Wash &amp; Fold Sign</title>
<link href="https://fonts.googleapis.com/css2?family=Anton&family=Kalam:wght@400&display=swap" rel="stylesheet">
<style>
  :root {
    --navy: #24449b;
    --sky: #8ab8e3;
    --wave-light: #a9cdee;
    --wave-mid: #6fa4da;
    --orange: #f06424;
    --paper: #ffffff;
  }
  html, body {
    margin: 0;
    padding: 0;
    width: 786px;
    height: 1200px;
    overflow: hidden;
    background: var(--paper);
  }
  .sign {
    position: relative;
    width: 786px;
    height: 1200px;
    overflow: hidden;
    background: var(--paper);
  }
  .sign-art {
    position: absolute;
    inset: 0;
    width: 786px;
    height: 1200px;
  }
  .brand-name {
    font-family: "Anton", sans-serif;
    font-size: 58px;
    fill: var(--navy);
    letter-spacing: 1px;
  }
  .headline-free,
  .headline-free-shadow {
    font-family: "Anton", sans-serif;
    font-size: 380px;
  }
  .headline-free {
    fill: var(--sky);
    stroke: var(--navy);
    stroke-width: 9px;
    paint-order: stroke;
    stroke-linejoin: miter;
  }
  .headline-free-shadow { fill: var(--navy); }
  .service-line {
    font-family: "Anton", sans-serif;
    font-size: 131px;
    fill: var(--navy);
  }
  .urgency-line {
    font-family: "Kalam", cursive;
    font-size: 150px;
    fill: var(--orange);
  }
  .wave-light { fill: var(--wave-light); }
  .wave-mid { fill: var(--wave-mid); }
  .wave-deep { fill: var(--navy); }
  .direction-arrow {
    fill: var(--orange);
    stroke: var(--navy);
    stroke-width: 9px;
    stroke-linejoin: miter;
  }
</style>
</head>
<body>
<main class="sign">
  <svg class="sign-art" viewBox="0 0 786 1200" xmlns="http://www.w3.org/2000/svg">
    <defs>
      <linearGradient id="bubbleTone" x1="0" y1="0" x2="0" y2="1">
        <stop offset="0%" stop-color="#c4def5"/>
        <stop offset="55%" stop-color="#8fbbe6"/>
        <stop offset="100%" stop-color="#4f78c0"/>
      </linearGradient>
    </defs>

    <g class="brand">
      <rect x="200" y="96" width="36" height="36" fill="var(--orange)"/>
      <text class="brand-name" x="250" y="138">Fresh Fold Laundry</text>
    </g>

    <text class="headline-free-shadow" x="27" y="562" textLength="744" lengthAdjust="spacingAndGlyphs">FREE</text>
    <text class="headline-free" x="20" y="555" textLength="744" lengthAdjust="spacingAndGlyphs">FREE</text>

    <text class="service-line" x="22" y="693" textLength="736" lengthAdjust="spacingAndGlyphs">WASH &amp; FOLD SERVICE</text>

    <text class="urgency-line" x="38" y="842" textLength="693" lengthAdjust="spacingAndGlyphs">Right Now!!</text>

    <path class="wave-light" d="M0,888 C150,860 300,900 440,960 C580,1020 700,1000 786,950 L786,1200 L0,1200 Z"/>
    <path class="wave-mid" d="M0,940 C170,920 330,985 470,1035 C610,1080 720,1030 786,985 L786,1200 L0,1200 Z"/>
    <path class="wave-deep" d="M0,1050 C160,1030 320,1080 470,1110 C620,1140 720,1060 786,960 L786,1200 L0,1200 Z"/>

    <rect class="bubble-area" x="46" y="892" width="138" height="276" rx="14" fill="url(#bubbleTone)" opacity="0.85" role="img" aria-label="Cluster of rising soap bubbles"/>

    <path class="direction-arrow" d="M340,922 L566,922 L566,876 L714,983 L566,1090 L566,1044 L340,1044 Z"/>
  </svg>
</main>
</body>
</html>
```